Unique Mendrix Building Bussiness Card Design

www.mendrix.com.au

Please see website for Company profile. We require a design that incorporates our logo colours and is unique in shape and style compared to all other business cards.

www.mendrix.com.au

INSPIRE US !!!
Updates

Target Market(s)

Facility managers, Building Managers, Architects

Industry/Entity Type

Business

Contact Information for Business Card

Mendrix Building Solutions
Project Manager
Dennis Harwood
0437 619 204
Sales@mendrix.com.au

Logo Text

Mendrix Building Solutions

Logo styles of interest
Abstract Logo
Requirements
Nice to have
• Card must show we are an established big business to trust.

```html
<!DOCTYPE html>
<html lang="en">
<head>
<meta charset="utf-8">
<title>Mendrix Building Solutions – Business Card</title>
<link href="https://fonts.googleapis.com/css2?family=Cabin:wght@400;600;700&display=swap" rel="stylesheet">
<style>
  :root {
    --stage: #e6e7e9;
    --card-white: #ffffff;
    --orange-light: #f38a1c;
    --orange-deep: #d9481a;
    --red-dark: #9c1a14;
    --accent-red: #d42a26;
    --brand-blue: #1f78b0;
    --ink: #333a40;
    --ink-soft: #5a6168;
    --sky-top: #8fb9e2;
    --sky-mid: #d7c7a8;
    --water: #6f93a8;
  }
  * { box-sizing: border-box; margin: 0; padding: 0; }
  html, body { width: 1200px; height: 900px; overflow: hidden; }
  body {
    background: var(--stage);
    font-family: "Cabin", sans-serif;
    position: relative;
  }
  .card {
    position: absolute;
    left: 300px;
    width: 600px;
    height: 343px;
    border-radius: 4px;
    overflow: hidden;
    box-shadow: 0 6px 18px rgba(0,0,0,0.18);
  }
  /* Back side */
  .card--back {
    top: 70px;
    background: linear-gradient(125deg, var(--orange-light) 0%, var(--orange-deep) 55%, var(--red-dark) 100%);
  }
  .card--back .brand-name {
    position: absolute;
    right: 44px;
    bottom: 78px;
    font-weight: 700;
    font-size: 48px;
    color: #f6efe6;
    letter-spacing: 0.5px;
  }
  /* Front side */
  .card--front {
    top: 487px;
    background: var(--card-white);
  }
  .card--front svg.band {
    position: absolute;
    inset: 0;
    width: 600px;
    height: 343px;
  }
  .contact {
    position: absolute;
    left: 34px;
    top: 120px;
    color: var(--ink);
  }
  .contact .person-name {
    font-size: 19px;
    font-weight: 400;
    letter-spacing: 1px;
    color: var(--brand-blue);
    text-transform: uppercase;
    line-height: 1.2;
  }
  .contact .role {
    font-size: 14px;
    color: var(--ink-soft);
    margin: 2px 0 8px;
  }
  .contact ul { list-style: none; }
  .contact li {
    display: flex;
    align-items: center;
    gap: 8px;
    font-size: 14px;
    line-height: 22px;
    color: var(--ink);
  }
  .contact li svg { width: 13px; height: 13px; flex: none; }
  .brand-block {
    position: absolute;
    right: 36px;
    bottom: 42px;
    text-align: right;
  }
  .brand-block .brand-name {
    font-weight: 700;
    font-size: 40px;
    color: var(--accent-red);
    line-height: 1;
  }
  .brand-block .tagline {
    margin-top: 10px;
    font-size: 15px;
    letter-spacing: 3.5px;
    color: var(--brand-blue);
    text-transform: uppercase;
  }
</style>
</head>
<body>

  <section class="card card--back" aria-label="Business card back">
    <div class="brand-name">Mendrix.com.au</div>
  </section>

  <section class="card card--front" aria-label="Business card front">
    <svg class="band" viewBox="0 0 600 343">
      <defs>
        <linearGradient id="cityTone" x1="0" y1="0" x2="0" y2="1">
          <stop offset="0" stop-color="var(--sky-top)"/>
          <stop offset="0.55" stop-color="var(--sky-mid)"/>
          <stop offset="1" stop-color="var(--water)"/>
        </linearGradient>
      </defs>
      <polygon points="0,0 600,0 600,206 0,36" fill="url(#cityTone)" role="img" aria-label="Photograph of a city skyline along a river at sunset"/>
      <line x1="0" y1="40" x2="600" y2="210" stroke="var(--accent-red)" stroke-width="5"/>
    </svg>

    <div class="contact">
      <div class="person-name">Dennis Harwood</div>
      <div class="role">Project Manager</div>
      <ul>
        <li>
          <svg viewBox="0 0 16 16"><circle cx="8" cy="8" r="8" fill="var(--brand-blue)"/><path d="M5 4.5l2 1.6-1 1.3a6 6 0 0 0 2.6 2.6l1.3-1 1.6 2-1 1a6.5 6.5 0 0 1-6.5-6.5z" fill="#fff"/></svg>
          0437 619 204
        </li>
        <li>
          <svg viewBox="0 0 16 16"><rect x="1" y="3" width="14" height="10" rx="1.5" fill="var(--brand-blue)"/><path d="M2 4.5l6 4.5 6-4.5" stroke="#fff" stroke-width="1.3" fill="none"/></svg>
          Sales@mendrix.com.au
        </li>
        <li>
          <svg viewBox="0 0 16 16"><circle cx="8" cy="8" r="7" fill="none" stroke="var(--brand-blue)" stroke-width="1.6"/><path d="M1 8h14M8 1c-3 3.5-3 10.5 0 14M8 1c3 3.5 3 10.5 0 14" stroke="var(--brand-blue)" stroke-width="1.2" fill="none"/></svg>
          www.mendrix.com.au
        </li>
      </ul>
    </div>

    <div class="brand-block">
      <div class="brand-name">Mendrix.com.au</div>
      <div class="tagline">Mendrix Building Solutions</div>
    </div>
  </section>

</body>
</html>
```